Brochure for Healthy Restaurant Concept

Please design a brochure for our meal prep menu . Include all items and all descriptions of the items . Include some photos. Please ensure you let us know what size paper your design will need to be printed on. Please make it a clean modern design, matching our logo and its ok to use other colors as well. We are open to designs. We dont want it to be too plain.

Include all items including the pre-built options, bundles, and custom meals on the brochure. I will include the old brochure to give you an example, don't copy items and prices from that particular brochure as they could be inaccurate for the "Pre-Built items and breakfast items now.

Industry/Entity Type

Restaurant

Requirements
Must have
• Logo, all menu items
Nice to have
• A QR code linking our website www.plumtreegrillhouse.com

```html
<!DOCTYPE html>
<html lang="en">
<head>
<meta charset="utf-8">
<title>Plum Tree Grill House – Meal Prep Menu Brochure</title>
<link rel="stylesheet" href="https://fonts.googleapis.com/css2?family=Oswald:wght@400;500;600&family=Lato:ital,wght@0,400;0,700;1,400&display=swap">
<style>
:root{
  --green:#7cb82f;
  --ink:#5d5d5d;
  --ink-soft:#7a7a7a;
  --paper:#f1f1f0;
  --paper-shade:#e6e6e5;
  --bar:#2b2b2b;
  --bg:#dcdcdc;
}
*{box-sizing:border-box;margin:0;padding:0}
html,body{width:1200px;height:857px;overflow:hidden;background:var(--bg)}
body{font-family:"Lato",sans-serif;color:var(--ink)}
.spread{position:absolute;left:40px;top:26px;width:1120px;height:792px;background:var(--paper);box-shadow:0 6px 24px rgba(0,0,0,.18);overflow:hidden}
.page{position:absolute;top:0;width:560px;height:792px}
.page--left{left:0}
.page--right{left:560px;background:linear-gradient(90deg,var(--paper-shade) 0,var(--paper) 40px)}
.fold{position:absolute;left:559px;top:0;width:2px;height:792px;background:rgba(0,0,0,.08)}
.bottom-bar{position:absolute;left:0;bottom:0;width:1120px;height:34px;background:var(--bar)}
.art{position:absolute;left:0;top:0}
.heading{font-family:"Oswald",sans-serif;text-transform:uppercase;line-height:1}
.menu-title{position:absolute;left:180px;top:48px;font-size:40px;font-weight:600;color:var(--green)}
.menu-title::after{content:"";display:block;width:36px;height:2px;background:var(--ink-soft);margin-top:8px}
.step{position:absolute;left:175px;width:300px;height:50px}
.step__num{position:absolute;left:0;top:0;width:48px;height:48px;border:2px solid var(--ink-soft);font-family:"Oswald",sans-serif;font-size:36px;font-weight:500;color:var(--ink);text-align:center;line-height:42px}
.step__title{position:absolute;left:60px;top:0;font-size:24px;font-weight:500;white-space:nowrap;color:var(--ink)}
.step__note{position:absolute;left:60px;top:30px;white-space:nowrap;font-style:italic;font-size:12px;line-height:1.15;color:var(--ink-soft)}
.list{position:absolute;font-style:italic;font-size:10.5px;line-height:13px;color:var(--ink)}
.list li{list-style:none;display:flex}
.list .name{flex:1;padding-right:6px}
.list .p{width:44px}
.list .p2{width:38px}
.cols{position:absolute;font-family:"Oswald",sans-serif;font-size:12px;color:var(--green);display:flex}
.cols span{width:44px}
.extras{position:absolute;left:485px;top:180px;width:200px;height:450px;border:1px solid #b9b9b9;padding:14px;font-size:10.5px;line-height:13px;font-style:italic}
.extras h4{font-style:normal;font-weight:400;font-size:11px;color:var(--green);display:flex;justify-content:space-between;margin:12px 0 4px}
.extras h4:first-child{margin-top:0}
.extras li{list-style:none;display:flex;justify-content:space-between}
.promo{margin-top:22px;font-size:16px;line-height:20px;font-style:normal}
.promo strong{color:var(--green);font-weight:700;display:block}
.breakfast{position:absolute;left:700px;top:228px;width:215px}
.breakfast h3{font-size:25px;font-weight:500;color:var(--ink);margin-bottom:12px}
.breakfast li{list-style:none;font-style:italic;font-size:10.5px;line-height:12.5px;margin-bottom:8px}
.app{position:absolute;left:930px;top:400px;width:175px}
.app h3{font-size:22px;font-weight:500;line-height:1.15;color:var(--ink)}
.app p{font-size:13px;line-height:16px;margin-top:10px;text-align:justify}
.badges{display:flex;gap:12px;margin-top:14px}
.badge{width:70px;height:22px;border-radius:4px;background:#3a3a3a}
.badge--light{background:#e0e0e0;border:1px solid #bcbcbc}
.visit{position:absolute;left:905px;top:612px;width:210px;font-size:14px;font-weight:500;line-height:1.25;color:var(--ink);text-align:center;white-space:nowrap}
.phone{position:absolute;top:665px;width:52px;height:90px;border-radius:9px;background:#4a4a4a;padding:4px}
.phone__screen{width:100%;height:100%;border-radius:6px}
.dot{position:absolute;border-radius:50%;background:var(--green)}
</style>
</head>
<body>
<main class="spread">
  <section class="page page--left">
    <svg class="art" width="560" height="792" viewBox="0 0 560 792">
      <polygon points="0,0 170,0 150,420 0,440" fill="#cfc3b4" role="img" aria-label="Photo of protein pancakes topped with banana slices, chocolate chips and chocolate drizzle"/>
      <polygon points="0,470 145,430 130,758 0,758" fill="var(--green)"/>
      <polygon points="0,440 150,420 148,432 0,470" fill="#d9d9d9"/>
    </svg>
    <h1 class="heading menu-title">Meal Prep Menu</h1>

    <div class="step" style="top:105px">
      <div class="step__num">01</div>
      <h2 class="heading step__title">Pick your protein</h2>
      <p class="step__note">If needing specific weights, please call</p>
    </div>
    <ul class="list" style="left:180px;top:162px;width:140px">
      <li><span class="name">8oz Striploin Steak</span><span class="p">$9.5</span></li>
      <li><span class="name">6oz Chicken Breast</span><span class="p">$5.5</span></li>
      <li><span class="name">6oz Salmon Fillet</span><span class="p">$7.25</span></li>
      <li><span class="name">4oz Ground Turkey</span><span class="p">$4.5</span></li>
      <li><span class="name">5oz Ground Bison</span><span class="p">$7.5</span></li>
      <li><span class="name">4oz Tofu</span><span class="p">$4</span></li>
    </ul>
    <ul class="list" style="left:332px;top:172px;width:140px">
      <li><span class="name">8oz Striploin Steak</span><span class="p">$9.5</span></li>
      <li><span class="name">6oz Chicken Breast</span><span class="p">$5.5</span></li>
      <li><span class="name">6oz Salmon Fillet</span><span class="p">$7.25</span></li>
      <li><span class="name">4oz Ground Turkey</span><span class="p">$4.5</span></li>
      <li><span class="name">5oz Ground Bison</span><span class="p">$7.5</span></li>
      <li><span class="name">4oz Tofu</span><span class="p">$4</span></li>
    </ul>

    <div class="step" style="top:252px">
      <div class="step__num">02</div>
      <h2 class="heading step__title">Pick your veggies</h2>
      <p class="step__note">If needing specific weights, please call</p>
    </div>
    <div class="cols" style="left:388px;top:300px"><span>100G</span><span>200G</span></div>
    <ul class="list" style="left:180px;top:316px;width:290px">
      <li><span class="name">Seasonal Veggies</span><span class="p">$2.5</span><span class="p p2">$4</span></li>
      <li><span class="name">Mixed Veggies (Broccoli, Cauliflower, Bell Peppers)</span><span class="p">$2.5</span><span class="p p2">$4</span></li>
      <li><span class="name">Carrots &amp; Peas</span><span class="p">$2.5</span><span class="p p2">$4</span></li>
      <li><span class="name">Broccoli &amp; Cauliflower</span><span class="p">$3</span><span class="p p2">$4.5</span></li>
      <li><span class="name">Bell Pepper Mix</span><span class="p">$2.5</span><span class="p p2">$4</span></li>
      <li><span class="name">The Green Mix (Broccoli, Green beans, Asparagus)</span><span class="p">$3.5</span><span class="p p2">$4.75</span></li>
      <li><span class="name">Asparagus</span><span class="p">$3.5</span><span class="p p2">$4.75</span></li>
      <li><span class="name">Green Beans</span><span class="p">$2.5</span><span class="p p2">$4</span></li>
      <li><span class="name">Broccoli</span><span class="p">$3</span><span class="p p2">$4.5</span></li>
      <li><span class="name">Carrots</span><span class="p">$2.5</span><span class="p p2">$4</span></li>
      <li><span class="name">Peas</span><span class="p">$2.5</span><span class="p p2">$4</span></li>
      <li><span class="name">Cauliflower</span><span class="p">$3</span><span class="p p2">$4.5</span></li>
      <li><span class="name">Custom Veggie Mix</span><span class="p">$3.5</span><span class="p p2">$4.75</span></li>
    </ul>

    <div class="step" style="top:530px">
      <div class="step__num">03</div>
      <h2 class="heading step__title">Pick your carbs</h2>
      <p class="step__note">If needing specific weights, please call</p>
    </div>
    <div class="cols" style="left:388px;top:580px"><span>100G</span><span>200G</span></div>
    <ul class="list" style="left:180px;top:596px;width:290px">
      <li><span class="name">Sweet potato</span><span class="p">$3</span><span class="p p2">$5</span></li>
      <li><span class="name">Penne Pasta (Gluten free available)</span><span class="p">$3</span><span class="p p2">$5</span></li>
      <li><span class="name">Brown Rice</span><span class="p">$3</span><span class="p p2">$5</span></li>
      <li><span class="name">Basmati Rice</span><span class="p">$3</span><span class="p p2">$5</span></li>
      <li><span class="name">Quinoa</span><span class="p">$3</span><span class="p p2">$5</span></li>
      <li><span class="name">Baby Potatoes</span><span class="p">$3</span><span class="p p2">$5</span></li>
      <li><span class="name">Strawberry Spinach Salad</span><span class="p">$6.5</span><span class="p p2">$8.5</span></li>
      <li><span class="name">Cranberry Pecan Salad</span><span class="p">$6.5</span><span class="p p2">$8.5</span></li>
    </ul>
  </section>

  <section class="page page--right">
    <svg class="art" width="560" height="792" viewBox="0 0 560 792">
      <polygon points="60,0 560,0 560,300 200,80" fill="#b7a58f" role="img" aria-label="Photo of healthy bowls with beets, asparagus, grains and fresh salad"/>
      <path d="M0,40 C120,40 200,70 240,110 C330,190 430,260 560,330 L560,370 C420,300 300,220 220,150 C160,100 90,80 0,80 Z" fill="var(--green)"/>
      <path d="M0,0 L60,0 C110,20 170,50 200,80 C140,50 70,40 0,40 Z" fill="var(--green)"/>
    </svg>
  </section>

  <div class="breakfast">
    <h3 class="heading">Breakfast Menu</h3>
    <ul>
      <li>Protein Blueberry Pancakes $10.5<br>Gluten free protein pancake mix, blueberries, 100% maple syrup, and yogurt blueberry sauce.</li>
      <li>Protein Chocolate Champ Pancakes $10<br>Gluten free protein pancake mix, chocolate chips, 100% maple syrup, and a house made chocolate sauce.</li>
      <li>Cinnamon Coco Waffle $10<br>Gluten Free Protein Pancake Mix, Cinnamon, Coconut flakes, paired with 100% maple syrup.</li>
      <li>Plain Protein Waffle $9<br>Gluten free protein waffle mix, with 100% maple syrup.</li>
      <li>Veggie Omelette $9.5<br>Eggs, bell peppers, spinach, tomato, mushroom, onion, &amp; Monterey Jack cheese.</li>
      <li>Mighty Meat Omelette $10.5<br>Bacon omelette, with bell peppers, onion, tomato and cheese.</li>
      <li>Classic Breakfast Sandwich $6.5<br>English muffin, 2 eggs, choice of zucchini hash brown or bacon, cheddar cheese, mayo, avocado, and tomato.</li>
      <li>Morning Muscle Burrito $10.5<br>Steak Bites, black beans, salsa, scrambled egg, cheese, all wrapped in a whole wheat tortilla.</li>
    </ul>
  </div>

  <aside class="extras">
    <h4>Add Sauces <span>$0.50</span></h4>
    <ul>
      <li>Sweet Chili Thai Sauce</li><li>Teriyaki Sauce</li><li>Chipotle Mayo</li><li>Sriracha Hot Sauce</li>
      <li>Pesto (Pasta Sauce)</li><li>Tomato Basil (Pasta Sauce)</li><li>Barbeque Sauce</li><li>Sweet and Sour</li>
      <li>Balsamic (Salad Dressing)</li><li>Gluten Free Teriyaki Sauce</li>
    </ul>
    <h4>Housemade Dressings <span>$1</span></h4>
    <ul><li>Sesame ginger vinaigrette</li><li>Lime ginger dill</li><li>Horseradish ranch</li></ul>
    <h4>Additional Options</h4>
    <ul>
      <li><span>Half Avocado</span><span>$2.5</span></li>
      <li><span>1oz. Cheese</span><span>$1.25</span></li>
      <li><span>1oz. Raw Onion</span><span>$1.00</span></li>
      <li><span>1oz. Raw Mushroom</span><span>$1.00</span></li>
    </ul>
    <p class="promo"><strong>Delivery available!<br>1 day notice needed</strong>Pick up fresh every time</p>
  </aside>

  <div class="app">
    <h3 class="heading">Order food<br>easily on our app</h3>
    <p>You can also download our mobile app from the app stores to choose your favorite meal from your favorite kitchen.</p>
    <div class="badges"><span class="badge"></span><span class="badge badge--light"></span></div>
  </div>
  <p class="heading visit">Visit us online at<br>www.plumtreegrillhouse.com</p>

  <div class="dot" style="left:1072px;top:712px;width:40px;height:40px"></div>
  <div class="dot" style="left:1092px;top:662px;width:10px;height:10px"></div>
  <div class="phone" style="left:912px"><div class="phone__screen" style="background:linear-gradient(#6b5a48,#3d3a36)" role="img" aria-label="App welcome screen for Plum Tree"></div></div>
  <div class="phone" style="left:975px;top:672px"><div class="phone__screen" style="background:linear-gradient(#f2f2f2 20%,#8a6f55 20%,#5e5c56)" role="img" aria-label="App home screen showing meal prep containers"></div></div>
  <div class="phone" style="left:1038px;top:678px"><div class="phone__screen" style="background:linear-gradient(#6d6a62 35%,#fafafa 35%)" role="img" aria-label="App meal selection screen"></div></div>

  <div class="fold"></div>
  <div class="bottom-bar"></div>
</main>
</body>
</html>
```